Vow Lanterns - Outdoor Ceremony Designs

We set up wedding ceremonies outside in parks in and beaches. The advert will be in magazines. The design needs to look trendy but sophisticated and show a range of our products in different locations. Here is our website if you need any idea's www.vowlanterns.com.au please ask questions.

Target Market(s)

Females ages 25 to 35

Industry/Entity Type

Wedding

Requirements
Must have
• Spec for the magazine that the ad will be going into:
• HALF PAGE (LANDSCAPE):
• 284MM X 95MM (Width x Height) NO BLEED
• SUPPLY
• ARTWORK SPECIFICATIONS
• SUBMITTING YOUR ARTWORK
• If you are providing us with your own artwork, it is your responsibility to make sure it is set up correctly and to all our required specifications. If it is not, you may be charged an additional fee. We have the right to refuse your artwork if it does not reflect the quality standard of our brochure.
• YOU CAN SEND YOUR ARTWORK VIA CD/DVD OR EMAIL
• ARTWORK SPECIFICATIONS
• Please supply a Commercial Print Ready PDF or JPEG document only.
• IMAGES: All images used in your artwork must be a resolution of 300dpi or above 1mb. Below this will not be accepted.
• FONTS: All fonts must be outlined and embedded. No fonts should go below 8pt for visibility purposes.
• COLOURS: CMYK not RGB. Please remove all spot colours; we will not accept artwork with spot colours.
• BLEED: Only required for a full page advertisement, no bleed is required on any of the other advertisement artwork sizes.
• If any changes need to be made to the clients existing artwork there maybe an additional fee charged and will be on a case by case basis. Please note that working art files will be required, for example a packaged idml or eps with fonts supplied.
• ADVERTISEMENT SELECTION
• 3. HALF PAGE (LANDSCAPE):
• BLEED IS ONLY REQUIRED FOR THE FULL PAGE, NO BLEED IS REQUIRED ON THE OTHER ADVERTISEMENT ARTWORK.
Nice to have
• Outdoor Ceremony Designs - Ph: 0472 318 694
• www.vowlanterns.com.au

```html
<!DOCTYPE html>
<html lang="en">
<head>
<meta charset="utf-8">
<title>Vow Lanterns – Outdoor Ceremony Designs</title>
<link href="https://fonts.googleapis.com/css2?family=Arimo:wght@400&display=swap" rel="stylesheet">
<style>
  :root {
    --page: #ffffff;
    --panel: #a5d6d7;
    --panel-soft: #c2e5e5;
    --ink: #161616;
    --frame: #ffffff;
    --shadow: rgba(0,0,0,0.35);
  }
  html, body {
    margin: 0;
    padding: 0;
    width: 1200px;
    height: 1200px;
    overflow: hidden;
    background: var(--page);
    font-family: "Arimo", Arial, sans-serif;
  }
  .advert {
    position: absolute;
    left: 10px;
    top: 366px;
    width: 1171px;
    height: 391px;
    background: var(--frame);
    box-shadow: 2px 2px 3px var(--shadow);
  }
  .gallery {
    position: absolute;
    left: 0;
    top: 3px;
    width: 378px;
    height: 385px;
  }
  .gallery .photo {
    position: absolute;
    width: 121px;
    height: 123px;
    box-shadow: 0 0 0 1px #e4e4e4;
  }
  .p1 { left: 0;     top: 0;     background: linear-gradient(180deg, #b9cde0 0%, #c9d6df 48%, #6a9a48 60%, #578c37 100%); }
  .p2 { left: 129px; top: 0;     background: linear-gradient(180deg, #6f9a58 0%, #c4a06c 38%, #c9bfb0 68%, #e6e3de 100%); }
  .p3 { left: 258px; top: 0;     background: linear-gradient(160deg, #3d6a2c 0%, #dfe5d8 55%, #2f5522 100%); }
  .p4 { left: 0;     top: 131px; background: linear-gradient(180deg, #345f2e 0%, #587f40 48%, #6aa040 62%, #4d8a30 100%); }
  .p5 { left: 129px; top: 131px; background: linear-gradient(180deg, #8d8452 0%, #6f8a55 38%, #c9cbbf 60%, #5a8f36 100%); }
  .p6 { left: 258px; top: 131px; background: linear-gradient(180deg, #ecebe0 0%, #1f3f2f 12%, #213f2d 66%, #9aa154 80%, #a6a85c 100%); }
  .p7 { left: 0;     top: 262px; background: linear-gradient(180deg, #4a7cb6 0%, #9dbcd9 35%, #4b7536 58%, #8a7556 80%, #64923e 100%); }
  .p8 { left: 129px; top: 262px; background: linear-gradient(180deg, #8cb5dc 0%, #3f7cae 28%, #5a8a40 48%, #d6dde6 68%, #e3e8ef 100%); }
  .p9 { left: 258px; top: 262px; background: linear-gradient(180deg, #4a7a34 0%, #d9d6cc 35%, #c8a873 60%, #5d8c3c 100%); }

  .panel {
    position: absolute;
    left: 380px;
    top: 0;
    width: 791px;
    height: 391px;
    background: var(--panel);
    overflow: hidden;
  }
  .panel .flourish {
    position: absolute;
    left: 300px;
    top: 0;
    width: 330px;
    height: 391px;
    background: radial-gradient(ellipse at 55% 60%, var(--panel-soft) 0%, rgba(194,229,229,0) 65%);
  }
  .brand {
    position: absolute;
    left: 14px;
    top: 92px;
    width: 324px;
    margin: 0;
    text-align: center;
    font-weight: 400;
    color: var(--ink);
    text-transform: uppercase;
    line-height: 1;
  }
  .brand .line {
    display: block;
    font-size: 42px;
    letter-spacing: 14px;
    padding-left: 14px;
  }
  .brand .line + .line { margin-top: 22px; }
  .contact {
    position: absolute;
    left: 6px;
    top: 340px;
    width: 372px;
    text-align: center;
    font-size: 11.5px;
    line-height: 14px;
    color: var(--ink);
    margin: 0;
  }
  .copy {
    position: absolute;
    left: 404px;
    top: 38px;
    font-size: 12.6px;
    line-height: 15.7px;
    color: var(--ink);
    white-space: nowrap;
  }
  .copy p { margin: 0 0 15.7px 0; }
</style>
</head>
<body>
  <section class="advert">
    <div class="gallery">
      <div class="photo p1" role="img" aria-label="Harbourside lawn ceremony with red carpet aisle, white chairs and palm trees"></div>
      <div class="photo p2" role="img" aria-label="Timber rotunda with white chairs and aisle runner on sandstone steps"></div>
      <div class="photo p3" role="img" aria-label="Close-up of white lily and rose floral arrangement"></div>
      <div class="photo p4" role="img" aria-label="Garden ceremony arch with white aisle runner and chairs"></div>
      <div class="photo p5" role="img" aria-label="White gazebo with rows of white chairs and aisle runner"></div>
      <div class="photo p6" role="img" aria-label="Row of tall conifer trees with LOVE letters on the lawn"></div>
      <div class="photo p7" role="img" aria-label="Park garden ceremony setting with palms under blue sky"></div>
      <div class="photo p8" role="img" aria-label="Clifftop ocean ceremony with white aisle and paper lanterns"></div>
      <div class="photo p9" role="img" aria-label="White ceremony chairs decorated with raffia bows"></div>
    </div>

    <div class="panel">
      <div class="flourish" role="img" aria-label="Faint floral swirl decoration"></div>
      <h1 class="brand"><span class="line">Vow</span><span class="line">Lanterns</span></h1>
      <p class="contact">info@vowlanterns.com.au &nbsp;|&nbsp; www.vowlanterns.com.au<br>Ph: 0472 318 694</p>
      <div class="copy">
        <p>Whether you are planning a garden wedding, a relaxed<br>coastal ceremony or a lavish affair, Vow Lanterns can<br>create your ceremony leaving your guests saying "wow"!</p>
        <p>We provide quality hire products, flexibility and attention to<br>detail. By choosing Vow Lanterns to style your special day<br>means you can be confident you have chosen the best. We<br>give you the option of meeting with us at your ceremony<br>location therefore giving you the peace of mind that your<br>special day will be everything you have dreamed of. Our aim<br>is to create a magical and stress free ceremony allowing you<br>to relax and enjoy your day.</p>
        <p>Let us give you memories to treasure for a lifetime. Browse<br>through our stylish packages or design a tailored package to<br>suit your budget and style.</p>
        <p>We are delighted you are considering Vow Lanterns for<br>your Wedding Day.</p>
      </div>
    </div>
  </section>
</body>
</html>
```